Need a book cover design for a Lumora Book on Herbal Remedies

I need a book cover for my new ebook, here are the details:
Title: Meadow Cures
Sub-Heading: Buried Ancient Garden Tonics
Reclaiming the Wisdom of Roots for Everyday Wellness and Strength
Author: Nora Belcourt

```html
<!DOCTYPE html>
<html lang="en">
<head>
<meta charset="utf-8">
<title>Meadow Cures – Nora Belcourt</title>
<link rel="stylesheet" href="https://fonts.googleapis.com/css2?family=Bebas+Neue&family=Playfair+Display:wght@400&display=swap">
<style>
  :root {
    --backdrop: #000000;
    --cover-orange: #F05A2C;
    --frame-gold: #E9B46A;
    --ink-white: #FFFFFF;
    --author-white: #F4EFEA;
  }
  html, body {
    margin: 0;
    padding: 0;
    width: 1200px;
    height: 1200px;
    overflow: hidden;
    background: var(--backdrop);
  }
  .cover {
    position: absolute;
    left: 230px;
    top: 44px;
    width: 740px;
    height: 1112px;
    background: var(--cover-orange);
    overflow: hidden;
  }
  .photo-row {
    position: absolute;
    left: 46px;
    width: 648px;
    height: 195px;
    display: flex;
    justify-content: space-between;
  }
  .photo-row--top { top: 53px; }
  .photo-row--bottom { top: 665px; }
  .photo-tile {
    width: 207px;
    height: 195px;
    box-sizing: border-box;
    border: 2px solid var(--frame-gold);
    border-radius: 13px;
  }
  .tile-garden-oils { background: linear-gradient(160deg, #6f9a3e, #3f5e22 55%, #8a6a2c); }
  .tile-mortar-herbs { background: linear-gradient(160deg, #5a4632, #8d6f4c 50%, #6b5a3a); }
  .tile-drying-flowers { background: linear-gradient(160deg, #3d4a5a, #8a5a3a 55%, #4a3a3a); }
  .tile-pot-herbs { background: linear-gradient(160deg, #7aa84a, #4e7a2e 55%, #8a5a30); }
  .tile-jars { background: linear-gradient(160deg, #4a5a3a, #b8a85a 50%, #7a5a6a); }
  .tile-sunlit-table { background: linear-gradient(160deg, #e8b060, #8aa040 50%, #b87040); }
  .title {
    position: absolute;
    left: 0;
    top: 0;
    width: 740px;
    height: 1112px;
    pointer-events: none;
  }
  .title text {
    font-family: "Bebas Neue", "Oswald", sans-serif;
    font-size: 238px;
    fill: var(--ink-white);
  }
  .subtitle {
    position: absolute;
    top: 903px;
    width: 100%;
    margin: 0;
    text-align: center;
    font-family: "Playfair Display", Georgia, serif;
    font-weight: 400;
    font-size: 37px;
    line-height: 50px;
    color: var(--ink-white);
  }
  .author {
    position: absolute;
    top: 995px;
    width: 100%;
    margin: 0;
    text-align: center;
    font-family: "Playfair Display", Georgia, serif;
    font-weight: 400;
    font-size: 64px;
    line-height: 80px;
    color: var(--author-white);
  }
</style>
</head>
<body>
  <main class="cover">
    <div class="photo-row photo-row--top">
      <div class="photo-tile tile-garden-oils" role="img" aria-label="Photo of herbs and oil bottles on a garden table"></div>
      <div class="photo-tile tile-mortar-herbs" role="img" aria-label="Photo of a wooden mortar and pestle among dried herbs"></div>
      <div class="photo-tile tile-drying-flowers" role="img" aria-label="Photo of hanging dried flowers above bottles and a bowl"></div>
    </div>

    <svg class="title" viewBox="0 0 740 1112" aria-label="Meadow Cures">
      <text x="46" y="452" textLength="648" lengthAdjust="spacingAndGlyphs">MEADOW</text>
      <text x="46" y="637" textLength="648" lengthAdjust="spacingAndGlyphs">CURES</text>
    </svg>

    <div class="photo-row photo-row--bottom">
      <div class="photo-tile tile-pot-herbs" role="img" aria-label="Photo of potted herbs, jars and a mortar outdoors"></div>
      <div class="photo-tile tile-jars" role="img" aria-label="Photo of corked glass jars filled with dried flowers"></div>
      <div class="photo-tile tile-sunlit-table" role="img" aria-label="Photo of herbs and bowls of spices on a sunlit table"></div>
    </div>

    <p class="subtitle">Buried Ancient Garden Tonics</p>
    <p class="author">Nora Belcourt</p>
  </main>
</body>
</html>
```